sommelier *

Sommelier Wine Hospitality Corvanne Star experience I'm working as a sommelier in a Corvanne Star restaurant. I try to reach People who are interested in invest in wine and wine loovers! In terms of color I would like to have a nice color based on a nice bordeaux red (as an advice). By the way i forgot to write my phone number and my email address. 439812604731 kdervin7@postiko.com I hope this info is enough so far.

```html
<!DOCTYPE html>
<html lang="en">
<head>
<meta charset="utf-8">
<title>Anselm Varga — Sommelier Business Card</title>
<link rel="stylesheet" href="https://fonts.googleapis.com/css2?family=Cinzel:wght@400;600&display=swap">
<style>
  :root {
    --backdrop: #2b2b2b;
    --card-top: #1d1d1d;
    --card-bottom: #0e0e0e;
    --silver: #c9c9c9;
    --silver-dim: #8d8d8d;
    --divider: #4a4a4a;
    --bordeaux: #8e1420;
    --bordeaux-deep: #5e0a12;
  }
  * { margin: 0; padding: 0; box-sizing: border-box; }
  html, body {
    width: 1200px;
    height: 928px;
    overflow: hidden;
    background: var(--backdrop);
  }
  .canvas {
    position: relative;
    width: 1200px;
    height: 928px;
    display: flex;
    flex-direction: column;
    align-items: center;
    justify-content: center;
    gap: 40px;
  }
  .card {
    position: relative;
    width: 660px;
    height: 378px;
    border-radius: 30px;
    background: linear-gradient(160deg, var(--card-top) 0%, var(--card-bottom) 100%);
  }
  .card-front {
    display: flex;
    align-items: center;
    justify-content: center;
  }
  .emblem {
    width: 50px;
    height: 96px;
    margin-top: -70px;
    border-radius: 6px;
    background: linear-gradient(180deg, var(--bordeaux) 0%, var(--bordeaux-deep) 45%, var(--silver-dim) 100%);
  }
  .card-back {
    display: flex;
    align-items: center;
    font-family: "Cinzel", serif;
    color: var(--silver);
  }
  .holder-name {
    width: 50%;
    padding-right: 24px;
    text-align: right;
    font-size: 26px;
    font-weight: 600;
    letter-spacing: 1.5px;
  }
  .divider {
    width: 1px;
    height: 82px;
    background: var(--divider);
  }
  .contact-list {
    list-style: none;
    padding-left: 28px;
    display: flex;
    flex-direction: column;
    gap: 14px;
    font-size: 15px;
    letter-spacing: 1px;
  }
  .contact-item {
    display: flex;
    align-items: center;
    gap: 14px;
  }
  .contact-icon {
    width: 16px;
    height: 16px;
    flex: none;
  }
</style>
</head>
<body>
<main class="canvas">
  <section class="card card-front">
    <div class="emblem" role="img" aria-label="Wine glass emblem filled with bordeaux red wine"></div>
  </section>

  <section class="card card-back">
    <h1 class="holder-name">Anselm Varga</h1>
    <div class="divider"></div>
    <ul class="contact-list">
      <li class="contact-item">
        <svg class="contact-icon" viewBox="0 0 16 16" aria-hidden="true">
          <rect x="4" y="1" width="8" height="14" rx="1.5" fill="none" stroke="#c9c9c9" stroke-width="1.3"/>
          <line x1="7" y1="12.5" x2="9" y2="12.5" stroke="#c9c9c9" stroke-width="1.2"/>
        </svg>
        <span>+439 812 604 731</span>
      </li>
      <li class="contact-item">
        <svg class="contact-icon" viewBox="0 0 16 16" aria-hidden="true">
          <rect x="1" y="3.5" width="14" height="9" fill="#c9c9c9"/>
          <polyline points="1,3.5 8,9 15,3.5" fill="none" stroke="#1a1a1a" stroke-width="1.1"/>
        </svg>
        <span>kdervin7@postiko.com</span>
      </li>
    </ul>
  </section>
</main>
</body>
</html>
```